Pura Senda Trek Holidays Rack Card

We need a double sided rack card design. One side should be promoting our "Seven Trail Days" tour with the flip side promoting our "Honeymoon" and "Custom & Family Tours". Colours should be in line with our website www.PuraSendaTrek.example. Text and photos attached (feel free to use as necessary). We are looking for a fun rack card that will catch clients eyes and hopefully promote Costa Rica as a fun and exciting vacation.

Target Market(s)

Tourism - USA and Canada

Industry/Entity Type

Tourism

Font styles to use
Sans Serif

Colors
0455a3
33a6d7
f37122

Requirements
Must have
• Our logo on both sides of the rack card. Must be bright and fun looking. Costa Rica is an outdoor destination with tons of fun activities to do, we want to try and get that feeling across on the card.
Nice to have
• I have added a price sticker to the attachments on this project. Is it possible to have something similar on the Seven Trail Days side? The price would be $1999 scored out with the new price being $1649.

```html
<!DOCTYPE html>
<html lang="en">
<head>
<meta charset="utf-8">
<title>Pura Senda Trek Holidays – Rack Card, Front and Back</title>
<link href="https://fonts.googleapis.com/css2?family=Oswald:wght@500;600&family=Arimo:wght@400;700&family=Kalam:wght@400&family=Noto+Serif:wght@400&family=Roboto+Slab:wght@700&display=swap" rel="stylesheet">
<style>
  :root{
    --brand-blue:#0455a3;
    --sky-blue:#33a6d7;
    --sunset-orange:#f37122;
    --navy:#0b2f66;
    --ink:#1d1d1d;
    --paper:#ffffff;
    --stage:#eef1f4;
    --gold:#ffd200;
  }
  *{box-sizing:border-box;margin:0;padding:0}
  html,body{width:1126px;height:1200px;overflow:hidden;background:var(--stage)}
  .rack-card{
    position:absolute;top:20px;width:530px;height:1160px;
    background:var(--paper);overflow:hidden;
    box-shadow:0 6px 24px rgba(0,0,0,.18);
    font-family:"Arimo",Arial,sans-serif;color:var(--ink);
  }
  .front{left:20px}
  .back{left:576px}

  /* ---------- front ---------- */
  .hero-photo{
    position:absolute;left:0;top:0;width:530px;height:320px;
    background:linear-gradient(160deg,#7fc6e6 0%,#3b8fc7 35%,#2f6e4a 60%,#9fd8ec 100%);
  }
  .title-banner{position:absolute;left:0;top:300px;width:530px;height:130px}
  .title-text{
    position:absolute;left:0;right:0;top:330px;text-align:center;
    font-family:"Oswald","Arial Narrow",sans-serif;font-weight:600;
    font-size:46px;letter-spacing:.5px;color:var(--paper);text-transform:uppercase;
  }
  .tagline{
    position:absolute;left:58px;top:432px;
    font-family:"Oswald","Arial Narrow",sans-serif;font-weight:500;
    font-size:30px;color:var(--brand-blue);text-transform:uppercase;
  }
  .script-line{
    position:absolute;left:132px;top:478px;
    font-family:"Kalam",cursive;font-size:38px;color:var(--sunset-orange);transform:rotate(-3deg);
  }
  .intro{
    position:absolute;left:36px;right:36px;top:566px;text-align:center;
    font-weight:700;font-size:18.5px;line-height:1.25;color:var(--sky-blue);text-transform:uppercase;
  }
  .itinerary{position:absolute;left:34px;top:668px;width:486px;list-style:none;font-size:19px;line-height:25px}
  .itinerary li{padding-left:74px;text-indent:-74px;margin-bottom:6px}
  .itinerary .day{font-weight:700;color:var(--brand-blue)}
  .price-sticker{position:absolute;left:338px;top:612px;width:176px;height:170px}
  .price-sticker .now{position:absolute;left:0;right:0;top:46px;text-align:center;color:#fff;font-weight:700;font-size:16px}
  .price-sticker .new{position:absolute;left:0;right:0;top:63px;text-align:center;color:#fff;font-weight:700;font-size:30px}
  .price-sticker .old{position:absolute;left:0;right:0;top:101px;text-align:center;color:var(--gold);font-weight:700;font-size:16px;text-decoration:line-through}
  .price-sticker .before{position:absolute;left:96px;top:119px;color:#fff;font-size:11px}
  .deco-left{position:absolute;left:8px;top:1026px;width:74px;height:60px;border-radius:30px;background:linear-gradient(135deg,#dfe8ee,#b8c8d4)}
  .deco-right{position:absolute;left:440px;top:1022px;width:82px;height:60px;border-radius:30px;background:linear-gradient(135deg,#f2b44a,#8a5a2b)}
  .brand-name{
    position:absolute;left:0;right:0;top:1024px;text-align:center;
    font-weight:700;font-size:28px;color:var(--sunset-orange);letter-spacing:2px;
  }
  .web-address{position:absolute;left:0;right:0;top:1066px;text-align:center;font-weight:700;font-size:19px;color:var(--navy)}
  .contact-bar{
    position:absolute;left:0;bottom:0;width:530px;height:52px;background:var(--navy);
    display:flex;align-items:center;justify-content:space-around;color:#fff;font-size:18px;
  }
  .contact-bar span{display:flex;align-items:center;gap:9px}
  .contact-bar .phone{font-weight:700}

  /* ---------- back ---------- */
  .scenery-photo{
    position:absolute;left:0;top:0;width:530px;height:400px;
    background:linear-gradient(180deg,#2c8fe0 0%,#8fc8ef 30%,#3f8a3a 60%,#7a7f6e 100%);
  }
  .back-panel{position:absolute;left:0;top:330px;width:530px;height:120px}
  .back-brand{
    position:absolute;left:0;right:0;top:420px;display:flex;justify-content:center;align-items:center;gap:12px;
    font-weight:700;font-size:34px;color:var(--sunset-orange);letter-spacing:2px;
  }
  .back-brand .dot{width:30px;height:30px;border-radius:50%;background:var(--sky-blue)}
  .about{
    position:absolute;left:40px;right:40px;top:492px;
    font-family:"Noto Serif",Georgia,serif;font-size:17.5px;line-height:27px;color:#222;
  }
  .about p{margin-bottom:12px}
  .family-photo{
    position:absolute;left:0;top:760px;width:530px;height:200px;
    background:linear-gradient(180deg,#9fd9ee 0%,#e6c9a8 60%,#d98a7a 100%);
  }
  .wave-band{position:absolute;left:0;top:880px;width:530px;height:150px}
  .family-inset{
    position:absolute;left:30px;top:900px;width:150px;height:150px;border-radius:50%;
    border:6px solid #fff;background:linear-gradient(160deg,#6fc3e8,#e7b8a0);
  }
  .family-heading{
    position:absolute;left:0;right:0;top:1048px;text-align:center;
    font-family:"Roboto Slab",Georgia,serif;font-weight:700;font-size:21px;line-height:26px;
    color:var(--brand-blue);text-transform:uppercase;letter-spacing:1px;
  }
  .web-bar{
    position:absolute;left:0;bottom:0;width:530px;height:52px;background:var(--navy);
    display:flex;align-items:center;justify-content:center;color:#fff;font-weight:700;font-size:18px;
  }
</style>
</head>
<body>

<section class="rack-card front">
  <div class="hero-photo" role="img" aria-label="Collage of adventure photos: rafters in helmets on whitewater, a zipliner in a harness, snorkelers in clear water"></div>

  <div class="title-banner">
    <svg width="530" height="130" viewBox="0 0 530 130">
      <polygon points="0,20 530,0 530,92 0,104" fill="#0455a3"/>
      <polygon points="50,104 530,92 530,104 50,118" fill="#33a6d7"/>
    </svg>
  </div>
  <div class="title-text">Seven Trail Days</div>

  <div class="tagline">8 Days, 8 Adventures, 1 Life</div>
  <div class="script-line">Let the journey begin...</div>

  <p class="intro">Come join us in the tropics on one of our all inclusive 8 day Seven Trail Days tours.</p>

  <ul class="itinerary">
    <li><span class="day">DAY 1</span> – Pick Up San Jose<br>International Airport</li>
    <li><span class="day">DAY 2</span> – Beginner Kayaking</li>
    <li><span class="day">DAY 3</span> – Whitewater Rafting.<br>Overnight Jungle Lodge</li>
    <li><span class="day">DAY 4</span> – Canopy/Zipline Tour &amp; Jungle Hikes.<br>Overnight Jungle Lodge</li>
    <li><span class="day">DAY 5</span> – Whitewater Rafting &amp; Beach</li>
    <li><span class="day">DAY 6</span> – Surfing &amp; Snorkeling</li>
    <li><span class="day">DAY 7</span> – Canyoning (Rappelling Waterfalls) or<br>Mountain Biking. Your choice!</li>
    <li><span class="day">DAY 8</span> – Drop Off San Jose International Airport</li>
  </ul>

  <div class="price-sticker">
    <svg width="176" height="170" viewBox="0 0 176 170">
      <polygon points="88,4 110,56 172,60 124,100 140,164 88,130 36,164 52,100 4,60 66,56" fill="#f37122" stroke="#f37122" stroke-width="6" stroke-linejoin="round"/>
    </svg>
    <div class="now">NOW</div>
    <div class="new">$1649</div>
    <div class="old">$1999</div>
    <div class="before">Before</div>
  </div>

  <div class="deco-left" role="img" aria-label="White starfish on sand"></div>
  <div class="deco-right" role="img" aria-label="Orange starfish and seashell"></div>
  <div class="brand-name">Pura Senda</div>
  <div class="web-address">www.PuraSendaTrek.example</div>

  <div class="contact-bar">
    <span class="phone">
      <svg width="20" height="20" viewBox="0 0 20 20"><circle cx="10" cy="10" r="8.5" fill="none" stroke="#fff" stroke-width="1.5"/><path d="M7 5.5l1.6 2.4-1 1c.6 1.3 1.5 2.2 2.6 2.7l1-1 2.3 1.6-.8 1.6c-3.3-.3-6.3-3.3-6.5-6.7z" fill="#fff"/></svg>
      1-888-555-0148
    </span>
    <span class="email">
      <svg width="20" height="20" viewBox="0 0 20 20"><circle cx="10" cy="10" r="8.5" fill="none" stroke="#fff" stroke-width="1.5"/><rect x="5.5" y="7" width="9" height="6.5" fill="none" stroke="#fff" stroke-width="1.2"/><path d="M5.5 7l4.5 3.5L14.5 7" fill="none" stroke="#fff" stroke-width="1.2"/></svg>
      info@PuraSendaTrek.example
    </span>
  </div>
</section>

<section class="rack-card back">
  <div class="scenery-photo" role="img" aria-label="Tropical scene with blue sky, palm trees, jungle and a waterfall over rocks"></div>

  <div class="back-panel">
    <svg width="530" height="120" viewBox="0 0 530 120">
      <polygon points="0,40 530,90 530,120 0,120" fill="#f37122"/>
      <polygon points="0,56 530,104 530,120 0,120" fill="#ffffff"/>
    </svg>
  </div>

  <div class="back-brand"><span class="dot"></span>Pura Senda</div>

  <div class="about">
    <p>Pura Senda is a tour company specializing in helping plan unique vacations. We are based in Costa Rica 365 days a year and can find the best activities, hotels and tours for your vacation/honeymoon desires.</p>
    <p>Our guides have enjoyed many of the region's best adventures and will give you the best advice.</p>
    <p>Tell us what you are looking for and we'll come up with a plan just for you!</p>
  </div>

  <div class="family-photo" role="img" aria-label="Children in snorkel masks and fins on a sunny beach"></div>

  <div class="wave-band">
    <svg width="530" height="150" viewBox="0 0 530 150">
      <path d="M0,60 C140,10 300,90 530,30 L530,150 L0,150 Z" fill="#33a6d7"/>
      <path d="M0,90 C160,40 320,120 530,60 L530,150 L0,150 Z" fill="#0455a3"/>
      <path d="M0,140 C160,110 340,150 530,120 L530,150 L0,150 Z" fill="#ffffff"/>
    </svg>
  </div>
  <div class="family-inset" role="img" aria-label="Round photo of two children in snorkel masks"></div>

  <div class="family-heading">Custom and<br>Family Tours</div>

  <div class="web-bar">www.PuraSendaTrek.example</div>
</section>

</body>
</html>
```